High-end residential home builder needs a business card design

We need a new business card design for a small residential construction company based in Boise, Idaho. We specialize in building custom high-end homes and remodels, with a focus on great design and craftsmanship.

We would like to use our current logo, but open to new color suggestions.
Just looking for a clean, sharp, modern design that looks high-end.

Target Market(s)

Upscale clientele

Industry/Entity Type

Contractor

Contact Information for Business Card

Company: Stonefield Custom Builders
Name: Marcus Tilley
Phone number: 208 367 4120
Email: MarcusTilleySCB@mailbox-example.com
Website: Stonefieldcustombuilders-example.com

Font styles to use
Serif
Sans Serif

Requirements
Must have
• Company Logo
Company name
My name
My phone number
My email
Company website
Nice to have
• I have attached a few photos of cards that I really like.

```html
<!DOCTYPE html>
<html lang="en">
<head>
<meta charset="utf-8">
<title>Stonefield Custom Builders – Business Card</title>
<link rel="stylesheet" href="https://fonts.googleapis.com/css2?family=Raleway:wght@500;600;700&family=Arimo:wght@400&display=swap">
<style>
  :root {
    --backdrop: #6e6e6e;
    --paper: #f6f6f6;
    --espresso: #2a1a0c;
    --amber: #d4832a;
    --ink: #555555;
    --rule: #9a9a9a;
    --gold-light: #d8962e;
    --gold-mid: #7a4a18;
  }
  * { box-sizing: border-box; margin: 0; padding: 0; }
  html, body {
    width: 1200px; height: 1200px; overflow: hidden;
    background: var(--backdrop);
  }
  .card {
    position: absolute; left: 262px; width: 686px; height: 392px;
    overflow: hidden;
  }
  .card-front { top: 165px; background: var(--paper); }
  .card-back { top: 653px; }

  .brand {
    position: absolute; left: 343px; top: 44px;
    display: flex; align-items: center; gap: 18px;
  }
  .brand-mark {
    width: 70px; height: 70px;
    border: 3px solid var(--espresso);
  }
  .brand-name {
    font-family: "Raleway", sans-serif; font-weight: 600;
    color: var(--espresso); letter-spacing: 0.28em; line-height: 1.35;
    font-size: 19px; white-space: nowrap;
  }
  .brand-name .line-sub { display: block; font-size: 12px; letter-spacing: 0.32em; }

  .holder-name {
    position: absolute; left: 45px; top: 264px;
    font-family: "Raleway", sans-serif; font-weight: 700;
    font-size: 24px; line-height: 30px; color: var(--amber); letter-spacing: 0.01em;
    white-space: nowrap;
  }
  .divider {
    position: absolute; left: 45px; top: 302px; width: 598px; height: 1px;
    background: var(--rule);
  }
  .contact {
    position: absolute; left: 45px; top: 314px;
    font-family: "Arimo", sans-serif; font-size: 15.5px; color: var(--ink);
    list-style: none; line-height: 19px; white-space: nowrap;
  }
  .contact li { display: flex; align-items: center; gap: 10px; }
  .contact svg { width: 12px; height: 12px; flex: none; }

  .footer-bands { position: absolute; left: 0; bottom: 0; width: 686px; height: 36px; }
  .website {
    position: absolute; left: 418px; top: 356px; height: 36px; width: 262px;
    font-family: "Arimo", sans-serif; font-size: 13.5px; line-height: 36px;
    color: #ffffff; white-space: nowrap; text-align: center;
  }

  .back-pattern {
    width: 100%; height: 100%;
    background: linear-gradient(100deg, var(--gold-light) 0%, var(--gold-mid) 38%, var(--espresso) 75%, #1f1308 100%);
  }
</style>
</head>
<body>
  <section class="card card-front">
    <div class="brand">
      <div class="brand-mark"></div>
      <div class="brand-name">STONEFIELD<span class="line-sub">CUSTOM BUILDERS</span></div>
    </div>

    <h1 class="holder-name">MARCUS TILLEY</h1>
    <div class="divider"></div>

    <ul class="contact">
      <li>
        <svg viewBox="0 0 12 12" aria-hidden="true"><path d="M2.5 0.5 L4.5 0.5 L5.3 3 L4 4.2 C4.7 5.8 6.2 7.3 7.8 8 L9 6.7 L11.5 7.5 L11.5 9.5 C11.5 10.8 10.5 11.5 9.5 11.5 C4.5 11 1 7.5 0.5 2.5 C0.5 1.4 1.2 0.5 2.5 0.5 Z" fill="#d4832a"/></svg>
        <span>208 367 4120</span>
      </li>
      <li>
        <svg viewBox="0 0 12 12" aria-hidden="true"><rect x="0.5" y="2.5" width="11" height="7.5" fill="#d4832a"/><path d="M0.8 3 L6 7 L11.2 3" fill="none" stroke="#f6f6f6" stroke-width="1"/></svg>
        <span>MarcusTilleySCB@mailbox-example.com</span>
      </li>
    </ul>

    <svg class="footer-bands" viewBox="0 0 686 36" aria-hidden="true">
      <rect x="0" y="24" width="400" height="12" fill="#2a1a0c"/>
      <polygon points="406,0 686,0 686,36 385,36" fill="#d4832a"/>
    </svg>
    <p class="website">Stonefieldcustombuilders-example.com</p>
  </section>

  <section class="card card-back">
    <div class="back-pattern" role="img" aria-label="Repeating embossed hexagon monogram pattern in gold foil on dark brown"></div>
  </section>
</body>
</html>
```